Law Offices business card

Hi there, I'll need business card for the Law Offices of Colby Marchetti. The information must convey his strategic approach and quick resolution to complex business litigation needs. Please emphasize Civil Litigation, Corporate Law, Business Governance and Real Estate Law. Colby has over 25 years of experience in these fields.The card should be modern and edgy and the message should be clear. Please consult his current website for ideas.

```html
<!DOCTYPE html>
<html lang="en">
<head>
<meta charset="utf-8">
<title>Law Offices of Colby Marchetti – Business Card</title>
<link rel="stylesheet" href="https://fonts.googleapis.com/css2?family=Tinos:wght@400;700&family=Open+Sans:wght@400&display=swap">
<style>
  :root {
    --page: #e6e4e0;
    --card: #f4f4f4;
    --ink: #1c1c1c;
    --ink-soft: #3a3a3a;
    --rule: #2a2a2a;
    --band: #3b4aa6;
    --band-text: #ffffff;
    --shadow: rgba(0, 0, 0, 0.18);
  }
  * { box-sizing: border-box; margin: 0; padding: 0; }
  html, body {
    width: 1200px; height: 902px; overflow: hidden;
    background: var(--page);
  }
  .sheet {
    width: 1200px; height: 902px;
    display: flex; flex-direction: column; align-items: center; justify-content: center;
    gap: 56px;
  }
  .card {
    position: relative;
    width: 620px; height: 354px;
    background: var(--card);
    box-shadow: 0 6px 18px var(--shadow);
    overflow: hidden;
  }
  .serif { font-family: "Tinos", "Times New Roman", serif; }
  .sans { font-family: "Open Sans", Tahoma, sans-serif; }

  /* Front */
  .firm-name {
    position: absolute; left: 44px; top: 44px;
    font-size: 31px; font-weight: 400; color: var(--ink);
    letter-spacing: 0.2px;
  }
  .attorney { position: absolute; left: 56px; top: 168px; }
  .attorney-name { font-size: 29px; font-weight: 700; color: var(--ink); }
  .attorney-role { font-size: 18px; color: var(--ink-soft); margin-top: 2px; }
  .divider {
    position: absolute; left: 352px; top: 112px;
    width: 1.5px; height: 106px; background: var(--rule);
  }
  .contacts {
    position: absolute; left: 372px; top: 104px;
    list-style: none;
  }
  .contacts li {
    display: flex; align-items: center; gap: 12px;
    font-size: 15.5px; color: var(--ink); height: 28px;
  }
  .contact-icon { width: 15px; height: 15px; flex: none; }
  .front-band { position: absolute; inset: 0; }
  .address { font-size: 16px; fill: var(--band-text); letter-spacing: 0.3px; }

  /* Back */
  .service-title {
    position: absolute; left: 40px; top: 52px;
    font-size: 46px; color: var(--ink); font-weight: 400;
  }
  .service-rule {
    position: absolute; left: 0; right: 0; top: 118px;
    height: 1.5px; background: var(--rule);
  }
  .service-list {
    position: absolute; left: 64px; top: 146px;
    list-style: none;
  }
  .service-list li {
    display: flex; align-items: center; gap: 18px;
    font-size: 21px; color: var(--ink-soft); letter-spacing: 1px;
    height: 42px;
  }
  .bullet { width: 14px; height: 14px; flex: none; }
</style>
</head>
<body>
<main class="sheet">

  <section class="card card-front" aria-label="Business card front">
    <h1 class="firm-name serif">Law offices of Colby Marchetti, P.A.</h1>

    <div class="attorney">
      <p class="attorney-name serif">Colby Marchetti</p>
      <p class="attorney-role sans">Attorney</p>
    </div>

    <div class="divider"></div>

    <ul class="contacts sans">
      <li>
        <svg class="contact-icon" viewBox="0 0 16 16"><rect width="16" height="16" fill="#1c1c1c"/><path d="M4.5 3.5l2 1.8-1 1.4c.8 1.6 2 2.8 3.6 3.6l1.4-1 1.8 2-1.3 1.4C7.8 12.4 3.6 8.2 3.4 4.8z" fill="#fff"/></svg>
        <span>561-380-4417</span>
      </li>
      <li>
        <svg class="contact-icon" viewBox="0 0 16 16"><rect width="16" height="16" fill="#1c1c1c"/><rect x="5" y="2.5" width="6" height="11" rx="1" fill="#fff"/><rect x="6" y="4" width="4" height="5" fill="#1c1c1c"/></svg>
        <span>561-902-7751</span>
      </li>
      <li>
        <svg class="contact-icon" viewBox="0 0 16 16"><rect width="16" height="16" fill="#1c1c1c"/><circle cx="8" cy="8" r="5" fill="none" stroke="#fff" stroke-width="1.3"/><path d="M3 8h10M8 3c-2.2 2.8-2.2 7.2 0 10M8 3c2.2 2.8 2.2 7.2 0 10" fill="none" stroke="#fff" stroke-width="1"/></svg>
        <span>www.marchettilegal.com</span>
      </li>
      <li>
        <svg class="contact-icon" viewBox="0 0 16 16"><rect width="16" height="16" fill="#1c1c1c"/><rect x="3" y="4.5" width="10" height="7" fill="none" stroke="#fff" stroke-width="1.2"/><path d="M3 4.5l5 4 5-4" fill="none" stroke="#fff" stroke-width="1.2"/></svg>
        <span>colby@marchettilegal.com</span>
      </li>
    </ul>

    <svg class="front-band" viewBox="0 0 620 354" aria-hidden="false">
      <path d="M40 354 Q330 258 620 226 L620 240 Q340 272 70 354 Z" fill="#1c1c1c"/>
      <path d="M0 354 Q320 268 620 248 L620 354 Z" fill="var(--band)"/>
      <path id="address-line" d="M150 344 Q370 284 610 262" fill="none"/>
      <text class="address sans"><textPath href="#address-line">318B Harbor Lane Coral Bay, Florida 33410</textPath></text>
    </svg>
  </section>

  <section class="card card-back" aria-label="Business card back">
    <h2 class="service-title serif">Service</h2>
    <div class="service-rule"></div>
    <ul class="service-list sans">
      <li><svg class="bullet" viewBox="0 0 14 14"><circle cx="7" cy="7" r="5.5" fill="none" stroke="#555" stroke-width="1"/><circle cx="7" cy="7" r="2.2" fill="#333"/></svg>Civil Litigation</li>
      <li><svg class="bullet" viewBox="0 0 14 14"><circle cx="7" cy="7" r="5.5" fill="none" stroke="#555" stroke-width="1"/><circle cx="7" cy="7" r="2.2" fill="#333"/></svg>Corporate Law</li>
      <li><svg class="bullet" viewBox="0 0 14 14"><circle cx="7" cy="7" r="5.5" fill="none" stroke="#555" stroke-width="1"/><circle cx="7" cy="7" r="2.2" fill="#333"/></svg>Real Estate Law</li>
      <li><svg class="bullet" viewBox="0 0 14 14"><circle cx="7" cy="7" r="5.5" fill="none" stroke="#555" stroke-width="1"/><circle cx="7" cy="7" r="2.2" fill="#333"/></svg>Business Governance</li>
    </ul>
  </section>

</main>
</body>
</html>
```